Use responsive design to make this page look and behave awesome in any size

YOU CAN SUBMIT PSD, HOWEVER, THE WINNER MUST SUBMIT PROVIDE A SINGLE CODED PAGE PER THE LINK AND INSTRUCTIONS AT THE BOTTOM OF THIS BRIEF. While developing an internal website, we realized we are not super great at making things look awesome and responsive for phone/tablet/desktop. Thats where you come in. We want you to take this code, Fork it, and then make it look awesome and work great on any size device.

Task at hand:

This page is a simple dashboard showing how a number of stores stack up against each other and against a corporate goal.

Top: Goal title, and where the logged in person's store stands in the ranking.
Green means you are in compliance
Red means you are not in compliance

Middle: Description of goal. Words to describe what the corporate goal is, and a target number.

Bottom: Here we just want to show the top 10 and bottom 5 out of 100+ stores. if your in the top ten, you are highlighted. If your in the bottom 5, you will be highlighted there too. If you are in the middle, we would put the your store info between the top and bottom... indicating your in the middle.
Green means you they are in compliance
Red means they are not in compliance

Your Mission is not only to make this look fantastic and responsive, but to have usable code in there.

You don't need to do any logic. All we care about is look and feel and responsive behavior on different size browsers.

The winner obviously gets the prize, and hopefully can become a solid resource to do more of this type of thing for us in the future.

Instructions:
Go to this link: https://codewharf.example/edit/tpl-tallyboard-widget
Click on the blue Fork button. This will give you a new URL that you can paste back into the contest to review results for us to see your work.
Uploading pictures is not necessary as the responsive code is what is important here.

Good luck!

Number of Pages Required

1 page

Requirements
Must have
• The page must be responsive and look very professional AND game like.
Should not have
• plugins. just native code

```html
<!DOCTYPE html>
<html lang="en">
<head>
<meta charset="utf-8">
<title>Lead Measures – Scoreboard Layouts</title>
<link rel="stylesheet" href="https://fonts.googleapis.com/css2?family=Lato:wght@400&family=Montserrat:wght@300;400;500&display=swap">
<style>
  :root {
    --ink: #1f1f1f;
    --muted: #555;
    --green: #2ecc7f;
    --green-dark: #25b56c;
    --red: #e0474c;
    --red-fill: #dc3545;
    --line: #e4e4e4;
    --sky-left: #5a6fe2;
    --sky-right: #8b5be0;
    --page: #ffffff;
    --panel: #f7f7f9;
    --bar: #f1f1f1;
  }
  * { box-sizing: border-box; margin: 0; padding: 0; }
  html, body { width: 1200px; height: 692px; overflow: hidden; background: var(--page); }
  body { position: relative; font-family: "Montserrat", sans-serif; color: var(--ink); }

  .view-label {
    position: absolute; top: 26px; font-family: "Lato", sans-serif;
    font-size: 25px; font-weight: 400; color: #111; transform: translateX(-50%);
  }

  /* ---------- screens ---------- */
  .screen { position: absolute; overflow: hidden; background: var(--page); }
  .screen--desktop { left: 15px; top: 81px; width: 890px; height: 550px; border: 1px solid #cfcfcf; }
  .screen--mobile { left: 920px; top: 81px; width: 268px; height: 550px; }

  .hero { position: absolute; left: 0; top: 0; width: 100%;
    background: linear-gradient(90deg, var(--sky-left), var(--sky-right)); }
  .screen--desktop .hero { height: 213px; }
  .screen--mobile .hero { height: 219px; }

  .bubble { position: absolute; border-radius: 50%; background: rgba(255,255,255,.22); }

  .hero-title { position: absolute; left: 0; width: 100%; text-align: center;
    color: #fff; font-weight: 300; letter-spacing: .3px; }
  .screen--desktop .hero-title { top: 48px; font-size: 27px; }
  .screen--mobile .hero-title { top: 24px; font-size: 16px; }

  .scroll-track { position: absolute; right: 0; top: 0; width: 7px; background: #f0f0f0; }
  .scroll-thumb { position: absolute; left: 1px; width: 5px; background: #c2c2c2; border-radius: 2px; }

  .console-bar { position: absolute; left: 0; bottom: 0; width: 100%; height: 18px;
    background: var(--bar); border-top: 1px solid #d5d5d5; font-size: 7px; color: #444;
    padding: 5px 6px; font-family: "Lato", sans-serif; }
  .console-bar .info { position: absolute; right: 30px; top: 4px; color: #2d6bd8; }
  .console-bar .caret { position: absolute; right: 10px; top: 3px; }

  /* ---------- measure cards ---------- */
  .card { position: absolute; background: #fff; box-shadow: 0 1px 4px rgba(0,0,0,.12); overflow: hidden; }
  .card-head { display: flex; justify-content: center; align-items: center; gap: 14px;
    background: var(--green); color: #fff; font-weight: 500; }
  .card-brief { position: relative; color: #333; }
  .target { position: absolute; background: var(--green-dark); color: #fff; font-weight: 500;
    display: flex; align-items: center; justify-content: center; border-radius: 2px; }

  .rank-list { list-style: none; }
  .rank-row { display: flex; align-items: center; border: 1px solid var(--line); margin-top: -1px;
    background: #fff; box-shadow: 0 1px 2px rgba(0,0,0,.04); }
  .rank-row .pos { color: var(--ink); }
  .rank-row .store { flex: 1; }
  .is-behind .store, .is-behind .score { color: var(--red); }
  .is-ahead .store, .is-ahead .score { color: var(--green-dark); }
  .rank-row.is-you { background: var(--red-fill); border-color: var(--red-fill); }
  .rank-row.is-you .pos, .rank-row.is-you .store, .rank-row.is-you .score { color: #fff; }

  /* desktop sizing */
  .screen--desktop .card { top: 108px; width: 198px; height: 460px; }
  .screen--desktop .card-head { height: 36px; font-size: 13px; }
  .screen--desktop .card-brief { font-size: 9.6px; line-height: 12px; padding: 13px 60px 0 12px; }
  .screen--desktop .target { top: 12px; right: 32px; height: 20px; padding: 0 6px; font-size: 8.5px; }
  .screen--desktop .rank-list { margin: 0 12px; }
  .screen--desktop .rank-row { height: 33px; padding: 0 12px; font-size: 9.8px; }
  .screen--desktop .pos { width: 10px; margin-right: 4px; }
  .screen--desktop .brief-2 { height: 53px; }
  .screen--desktop .brief-3 { height: 65px; }
  .screen--desktop .brief-4 { height: 77px; }

  /* mobile sizing */
  .screen--mobile .card { left: 20px; width: 224px; }
  .screen--mobile .card-head { height: 38px; font-size: 13px; }
  .screen--mobile .card-brief { font-size: 9.8px; line-height: 13px; padding: 14px 70px 0 13px; }
  .screen--mobile .target { top: 14px; right: 38px; height: 20px; padding: 0 6px; font-size: 8.5px; }
  .screen--mobile .rank-list { margin: 0 17px 0 13px; }
  .screen--mobile .rank-row { height: 34px; padding: 0 12px; font-size: 10.4px; }
  .screen--mobile .pos { width: 10px; margin-right: 4px; }
  .card-scroll { position: absolute; right: 3px; width: 3px; background: #c9c9c9; }
</style>
</head>
<body>

<div class="view-label" style="left:446px">Desktop View</div>
<div class="view-label" style="left:1056px">Mobile View</div>

<!-- Desktop layout -->
<section class="screen screen--desktop">
  <div class="hero">
    <span class="bubble" style="left:62px;top:21px;width:60px;height:60px"></span>
    <span class="bubble" style="left:177px;top:-25px;width:88px;height:88px"></span>
    <span class="bubble" style="left:557px;top:20px;width:60px;height:60px"></span>
    <span class="bubble" style="left:773px;top:-15px;width:92px;height:92px"></span>
    <h1 class="hero-title">LEAD MEASURES</h1>
  </div>

  <article class="card" style="left:19px">
    <header class="card-head"><span>TEAM</span><span>92.1%</span></header>
    <div class="card-brief brief-2">Use Slow Stock wherever possible<span class="target">80%</span></div>
    <ol class="rank-list is-behind">
      <li class="rank-row"><span class="pos">1</span><span class="store">(1) yjcQbtCyQu</span><span class="score">1%</span></li>
      <li class="rank-row"><span class="pos">2</span><span class="store">(1) crsmicfXwS</span><span class="score">1%</span></li>
      <li class="rank-row"><span class="pos">3</span><span class="store">(2) wnLJojLRSf</span><span class="score">2%</span></li>
      <li class="rank-row"><span class="pos">4</span><span class="store">(2) swEbjeRrpi</span><span class="score">2%</span></li>
      <li class="rank-row"><span class="pos">5</span><span class="store">(4) oUauMPncOA</span><span class="score">4%</span></li>
      <li class="rank-row"><span class="pos">6</span><span class="store">(5) vYuFdHZExR</span><span class="score">5%</span></li>
      <li class="rank-row"><span class="pos">7</span><span class="store">(5) jvBnNaGkeE</span><span class="score">5%</span></li>
      <li class="rank-row"><span class="pos">8</span><span class="store">(6) CuWIlvexCs</span><span class="score">6%</span></li>
      <li class="rank-row"><span class="pos">9</span><span class="store">(7) GucpFDVVJP</span><span class="score">7%</span></li>
      <li class="rank-row"><span class="pos">10</span><span class="store">(7) zzFPomjINi</span><span class="score">7%</span></li>
    </ol>
  </article>

  <article class="card" style="left:235px">
    <header class="card-head"><span>SLOW</span><span>0%</span></header>
    <div class="card-brief brief-3">Less than 0% of inventory slower than 100 days<span class="target">&lt; 1%</span></div>
    <ol class="rank-list">
      <li class="rank-row is-ahead"><span class="pos">1</span><span class="store">(80) GaccDehKUO</span><span class="score">0%</span></li>
      <li class="rank-row is-ahead"><span class="pos">2</span><span class="store">(97) YqyVfKITIl</span><span class="score">0%</span></li>
      <li class="rank-row is-ahead"><span class="pos">3</span><span class="store">(89) NZBGVulmnc</span><span class="score">0%</span></li>
      <li class="rank-row is-ahead"><span class="pos">4</span><span class="store">(67) PvQdqyeaHr</span><span class="score">0%</span></li>
      <li class="rank-row is-ahead"><span class="pos">5</span><span class="store">(55) aPfpNcqcDh</span><span class="score">0%</span></li>
      <li class="rank-row is-you"><span class="pos">6</span><span class="store">(00) Your Store</span><span class="score">2%</span></li>
      <li class="rank-row is-behind"><span class="pos">7</span><span class="store">(20) DZQteMnWQo</span><span class="score">2%</span></li>
      <li class="rank-row is-behind"><span class="pos">8</span><span class="store">(19) mXZyxOltGl</span><span class="score">2%</span></li>
      <li class="rank-row is-behind"><span class="pos">9</span><span class="store">(11) QSESmpDJqw</span><span class="score">2%</span></li>
      <li class="rank-row is-behind"><span class="pos">10</span><span class="store">(71) nIlaXFpJWv</span><span class="score">2%</span></li>
    </ol>
  </article>

  <article class="card" style="left:451px">
    <header class="card-head"><span>TURNS</span><span>2.2</span></header>
    <div class="card-brief brief-2">Turn inventory 6 or more times a year<span class="target">&gt; 6</span></div>
    <ol class="rank-list is-behind">
      <li class="rank-row"><span class="pos">1</span><span class="store">(8) VZaEOSVkef</span><span class="score">0.2</span></li>
      <li class="rank-row"><span class="pos">2</span><span class="store">(3) PcVKNpUNmj</span><span class="score">0.2</span></li>
      <li class="rank-row"><span class="pos">3</span><span class="store">(4) RllyRZsTIn</span><span class="score">0.4</span></li>
      <li class="rank-row"><span class="pos">4</span><span class="store">(9) epiNQFtERO</span><span class="score">0.6</span></li>
      <li class="rank-row"><span class="pos">5</span><span class="store">(3) FbFOzkjSpF</span><span class="score">0.7</span></li>
      <li class="rank-row"><span class="pos">6</span><span class="store">(1) DiilXiGkTx</span><span class="score">0.8</span></li>
      <li class="rank-row"><span class="pos">7</span><span class="store">(7) RdzzkcVqtC</span><span class="score">0.8</span></li>
      <li class="rank-row"><span class="pos">8</span><span class="store">(4) UyzYfilMzU</span><span class="score">0.8</span></li>
      <li class="rank-row"><span class="pos">9</span><span class="store">(1) jxWbwORyVa</span><span class="score">0.8</span></li>
      <li class="rank-row"><span class="pos">10</span><span class="store">(7) SCXulMdjcB</span><span class="score">1</span></li>
    </ol>
  </article>

  <article class="card" style="left:666px">
    <header class="card-head"><span>VALUES</span><span>1.9</span></header>
    <div class="card-brief brief-4">Inventory Value to be around 1.25 x you last months INVENTORY sales<span class="target">1.25</span></div>
    <ol class="rank-list is-ahead">
      <li class="rank-row"><span class="pos">1</span><span class="store">(8) VZaEOSVkef</span><span class="score">0.2</span></li>
      <li class="rank-row"><span class="pos">2</span><span class="store">(3) PcVKNpUNmj</span><span class="score">0.2</span></li>
      <li class="rank-row"><span class="pos">3</span><span class="store">(4) RllyRZsTIn</span><span class="score">0.4</span></li>
      <li class="rank-row"><span class="pos">4</span><span class="store">(9) epiNQFtERO</span><span class="score">0.6</span></li>
      <li class="rank-row"><span class="pos">5</span><span class="store">(3) FbFOzkjSpF</span><span class="score">0.7</span></li>
      <li class="rank-row"><span class="pos">6</span><span class="store">(1) DiilXiGkTx</span><span class="score">0.8</span></li>
      <li class="rank-row"><span class="pos">7</span><span class="store">(7) RdzzkcVqtC</span><span class="score">0.8</span></li>
      <li class="rank-row"><span class="pos">8</span><span class="store">(4) UyzYfilMzU</span><span class="score">0.8</span></li>
      <li class="rank-row"><span class="pos">9</span><span class="store">(1) jxWbwORyVa</span><span class="score">0.8</span></li>
      <li class="rank-row"><span class="pos">10</span><span class="store">(7) SCXulMdjcB</span><span class="score">1</span></li>
    </ol>
  </article>

  <div class="scroll-track" style="height:532px"><span class="scroll-thumb" style="top:0;height:358px"></span></div>

  <footer class="console-bar">Console<span class="info">&#9432; 1</span><span class="caret">&#8963;</span></footer>
</section>

<!-- Mobile layout -->
<section class="screen screen--mobile">
  <div class="hero">
    <h1 class="hero-title">LEAD MEASURES</h1>
  </div>

  <article class="card" style="top:59px;height:236px">
    <header class="card-head"><span>TEAM</span><span>92.1%</span></header>
    <div class="card-brief" style="height:55px">Use Slow Stock wherever possible<span class="target">80%</span></div>
    <ol class="rank-list is-behind">
      <li class="rank-row"><span class="pos">1</span><span class="store">(1) yjcQbtCyQu</span><span class="score">1%</span></li>
      <li class="rank-row"><span class="pos">2</span><span class="store">(1) crsmicfXwS</span><span class="score">1%</span></li>
      <li class="rank-row"><span class="pos">3</span><span class="store">(2) wnLJojLRSf</span><span class="score">2%</span></li>
      <li class="rank-row"><span class="pos">4</span><span class="store">(2) swEbjeRrpi</span><span class="score">2%</span></li>
      <li class="rank-row"><span class="pos">5</span><span class="store">(4) oUauMPncOA</span><span class="score">4%</span></li>
    </ol>
    <span class="card-scroll" style="top:38px;height:60px"></span>
  </article>

  <article class="card" style="top:312px;height:260px">
    <header class="card-head"><span>SLOW</span><span>0%</span></header>
    <div class="card-brief" style="height:67px">Less than 0% of inventory slower than 100 days<span class="target">&lt; 1%</span></div>
    <ol class="rank-list is-ahead">
      <li class="rank-row"><span class="pos">1</span><span class="store">(80) GaccDehKUO</span><span class="score">0%</span></li>
      <li class="rank-row"><span class="pos">2</span><span class="store">(97) YqyVfKITIl</span><span class="score">0%</span></li>
      <li class="rank-row"><span class="pos">3</span><span class="store">(89) NZBGVulmnc</span><span class="score">0%</span></li>
      <li class="rank-row"><span class="pos">4</span><span class="store">(67) PvQdqyeaHr</span><span class="score">0%</span></li>
    </ol>
    <span class="card-scroll" style="top:38px;height:66px"></span>
  </article>

  <div class="scroll-track" style="height:550px;background:#f4f4f4"><span class="scroll-thumb" style="top:0;height:290px"></span></div>
</section>

</body>
</html>
```